Upscale business cards needed for family business

We need professional business cards created for several family members. We are a family business holding company. We would like these relatively simple and straightforward, but also with a unique element to set them apart. Probably stick with neutral and simple colors - white, grey etc. We need space for the traditional elements, including name, title, address, email/phone number. And we will be creating several from this template so it needs to be template that is easy to switch information in and out of.

Industry/Entity Type

Business

Contact Information for Business Card

Please include the attached Dunmore Ventures logo.

Requirements
Must have
• The attached Dunmore Ventures logo.

```html
<!DOCTYPE html>
<html lang="en">
<head>
<meta charset="utf-8">
<title>Dunmore Ventures Stationery</title>
<link href="https://fonts.googleapis.com/css2?family=Cinzel:wght@500&family=Lato:wght@400;700&display=swap" rel="stylesheet">
<style>
  :root {
    --backdrop: #eeeeee;
    --paper: #ffffff;
    --ink: #1f1f1f;
    --ink-soft: #555555;
    --gold: #c9a227;
    --card-dark: #141414;
    --rule: #222222;
  }
  * { box-sizing: border-box; margin: 0; padding: 0; }
  html, body { width: 1200px; height: 820px; overflow: hidden; }
  body {
    background: var(--backdrop);
    font-family: "Lato", Arial, sans-serif;
    color: var(--ink);
    position: relative;
  }

  .brand-name {
    font-family: "Cinzel", Georgia, serif;
    font-weight: 500;
    color: var(--gold);
    letter-spacing: 0.06em;
    white-space: nowrap;
  }

  /* Letterhead */
  .letterhead {
    position: absolute;
    left: 80px; top: 40px;
    width: 520px; height: 736px;
    background: var(--paper);
    box-shadow: 0 2px 10px rgba(0,0,0,0.08);
    padding: 54px 56px 0;
    font-size: 9.5px;
    line-height: 1.55;
    color: var(--ink-soft);
  }
  .letterhead__brand { text-align: center; font-size: 19px; margin-bottom: 56px; }
  .letterhead__address { margin: 0 0 16px; }
  .letterhead__body p { margin-bottom: 12px; }
  .letterhead__signature {
    width: 120px; height: 34px; margin: 14px 0 2px;
    background: linear-gradient(90deg, #d9d9d9, #f2f2f2);
    border-radius: 3px;
  }
  .letterhead__role { color: var(--ink); font-weight: 700; }
  .letterhead__footer {
    position: absolute; right: 56px; bottom: 34px;
    text-align: right; font-size: 8px; color: var(--ink-soft);
  }
  .letterhead__footer .web { font-size: 9px; color: var(--ink); font-weight: 700; margin-bottom: 2px; }
  .letterhead__band-dark { position: absolute; left: 0; bottom: 0; width: 100%; height: 5px; background: var(--rule); }
  .letterhead__band-gold { position: absolute; right: 0; bottom: 5px; width: 150px; height: 9px; background: var(--gold); }

  /* Cards */
  .card {
    position: absolute;
    width: 420px; height: 240px;
    box-shadow: 0 2px 10px rgba(0,0,0,0.12);
  }
  .card--back { left: 680px; top: 150px; background: var(--paper); }
  .card--front { left: 680px; top: 460px; background: var(--card-dark); display: flex; align-items: center; justify-content: center; }
  .card--front .brand-name { font-size: 26px; }

  .card__brand { position: absolute; right: 36px; top: 34px; font-size: 15px; }
  .card__accent { position: absolute; right: 0; top: 0; width: 10px; height: 100%; background: var(--gold); }
  .card__accent-line { position: absolute; left: 0; bottom: 0; width: 100%; height: 3px; background: var(--rule); }
  .card__person { position: absolute; left: 36px; top: 104px; }
  .card__name { font-weight: 700; font-size: 14px; letter-spacing: 0.08em; color: var(--ink); }
  .card__title { font-size: 9px; color: var(--ink-soft); margin-bottom: 12px; letter-spacing: 0.05em; }
  .contact-list { list-style: none; font-size: 9px; color: var(--ink-soft); }
  .contact-list li { display: flex; align-items: center; gap: 7px; margin-bottom: 5px; }
  .contact-list svg { width: 10px; height: 10px; flex: none; }
</style>
</head>
<body>

<section class="letterhead">
  <div class="letterhead__brand brand-name">Dunmore Ventures</div>

  <p>November 1, 2019</p>
  <p class="letterhead__address">Mr. Peter Hale<br>48 Orchard Row<br>Fairview, FV 20451</p>
  <p style="margin-bottom:12px">Dear Mr. Hale:</p>

  <div class="letterhead__body">
    <p>The first paragraph of a typical business letter is used to state the main point of the letter. Begin with a friendly opening, then quickly transition into the purpose of your letter. Use a couple of sentences to explain the purpose, but do not go in to detail until the next paragraph.</p>
    <p>Beginning with the second paragraph, state the supporting details to justify your purpose. These may take the form of background information, statistics or first-hand accounts. A few short paragraphs within the body of the letter should be enough to support your reasoning. Finally, in the closing paragraph, briefly restate your purpose and why it is important.</p>
    <p>Finally, in the closing paragraph, briefly restate your purpose and why it is important. If the purpose of your letter is related to your employment, consider ending your letter with your contact information. Think about closing with gratitude for the reader's time.</p>
  </div>

  <p>Sincerely,</p>
  <div class="letterhead__signature" role="img" aria-label="Handwritten signature of the company president"></div>
  <p class="letterhead__role">President</p>

  <div class="letterhead__footer">
    <p class="web">www.dunmoreventures.com | www.dunmoregroup.com</p>
    <p>Dunmore Ventures is a family holding company managing long term investments and assets.</p>
  </div>
  <div class="letterhead__band-gold"></div>
  <div class="letterhead__band-dark"></div>
</section>

<section class="card card--back">
  <div class="card__brand brand-name">Dunmore Ventures</div>
  <div class="card__person">
    <p class="card__name">AARON WELLS</p>
    <p class="card__title">Managing Partner</p>
    <ul class="contact-list">
      <li>
        <svg viewBox="0 0 10 10"><path d="M2 1h2l1 2-1.2 1a5 5 0 0 0 2.2 2.2L7 5l2 1v2a1 1 0 0 1-1 1A7 7 0 0 1 1 2a1 1 0 0 1 1-1z" fill="var(--gold)"/></svg>
        +1 555 014 2280
      </li>
      <li>
        <svg viewBox="0 0 10 10"><rect x="0.5" y="2" width="9" height="6" fill="var(--gold)"/><path d="M0.5 2l4.5 3.5L9.5 2" stroke="#fff" fill="none" stroke-width="0.9"/></svg>
        aaron@dunmoreventures.com
      </li>
      <li>
        <svg viewBox="0 0 10 10"><path d="M5 0.5a3.3 3.3 0 0 0-3.3 3.3C1.7 6.3 5 9.5 5 9.5s3.3-3.2 3.3-5.7A3.3 3.3 0 0 0 5 0.5z" fill="var(--gold)"/><circle cx="5" cy="3.8" r="1.2" fill="#fff"/></svg>
        48 Orchard Row, Fairview, FV 20451
      </li>
    </ul>
  </div>
  <div class="card__accent"></div>
  <div class="card__accent-line"></div>
</section>

<section class="card card--front">
  <div class="brand-name">Dunmore Ventures</div>
</section>

</body>
</html>
```